Im looking for a sleek and sexy business card, that resembles elite or VIP status status.
our business is marnivoss.com
you can view our products on there, but our main audience for handing out our cards will be for people in the hospitality industry, so it will need to impress high management and CEO of hotels and restaurants, bars, clubs etc...
the card features will have UV spot on both sides, 400gsm stock. standard size.
Artwork should be 86 x 54mm + 2mm bleed = 90 x 58mm
it should have a nice "unique" uv spot pattern that highlights the card, not a repeated pattern, theres no originality there, and it will be disregarded.
The written material will be:
Marni Voss Hospitality College (logo)
Dena Whitby
Director
Phone: 1300 561 437
Mobile: 0439 817 265
Email: info@marnivoss.com
website: www.marnivoss.com
I'm looking for originality here, i don't want just a simple stock card, want something that has a wow factor for people.
You will find the logo attached. you may invert the white to black words to suit the background as you please.
thank you and good luck
As a side note, ive received a lot of proposals, im too busy to give feedback to each and every one, so if i havent provided feedback for your design within 24 hours, then consider it not acceptable, and you could resubmit another design.
So far i have not seen any design that stood out for me, they all seem pretty generic. there nothing thats unique, i would figure for the amount that im offering, that people would put some more effort and creativity into the design.
so far over 200 designs submitted, and nothing i have seen looks very original, everything looks like a different variation of the same stuff, i said it very clearly i wanted something unique, the only thing that has come close to it so far is this one
Reason: Ive received alot of design concepts and i have reviewed everyone, but i havent had time to give feedback to every single one, only the ones that have interested me, if i havent responded, its because i havent found it good enough.
so far only a few design have been on par with what ive been looking for, an attractive eye popping design.
heres a few of them,
http://files.pitchgallery.net/design_img/51846/62937/62937_2846105_51846_image.jpg
http://files.pitchgallery.net/design_img/51846/58714/58714_2846592_51846_image.jpg
theyre, both unique and original, and eye catching, the only thing theyre missing is the sexyness.
if you still think you have some creativity left in your minds, then throw it on here.
Reason: Sorry guys for the delay, I was in a serious accident and out of commission for the past few months, I'm just slowly recovering now, please bare with me as i try to attend to this project, it may take me awhile as I have other projects that are on standby, I'm not 100% at the moment, so im extending the deadline for 2 weeks right now. Thanks for your patience.

```html
<!DOCTYPE html>
<html lang="en">
<head>
<meta charset="utf-8">
<title>Marni Voss Hospitality College – Business Card</title>
<link rel="stylesheet" href="https://fonts.googleapis.com/css2?family=Open+Sans:wght@400;600;700&display=swap">
<style>
  :root {
    --page-bg: #e9e7e4;
    --card-dark-top: #3b3c3f;
    --card-dark-bottom: #141516;
    --card-blue-top: #1c5f9c;
    --card-blue-bottom: #071a33;
    --accent-blue: #4a9fe0;
    --edge-blue: #2c6fa8;
    --text-white: #ffffff;
    --text-grey: #b9bcc2;
    --bokeh-teal: rgba(110, 225, 230, 0.75);
    --bokeh-blue: rgba(40, 120, 220, 0.55);
  }
  * { margin: 0; padding: 0; box-sizing: border-box; }
  html, body {
    width: 1192px;
    height: 1200px;
    overflow: hidden;
    background: var(--page-bg);
    font-family: "Open Sans", Arial, sans-serif;
  }
  .sheet {
    position: relative;
    width: 1192px;
    height: 1200px;
  }
  .card {
    position: absolute;
    left: 166px;
    width: 860px;
    height: 540px;
    border-radius: 4px;
    overflow: hidden;
    box-shadow: 0 8px 24px rgba(0, 0, 0, 0.25);
  }
  .card--front {
    top: 40px;
    background: linear-gradient(160deg, var(--card-dark-top) 0%, #2a2b2e 45%, var(--card-dark-bottom) 100%);
  }
  .card--back {
    top: 620px;
    background: linear-gradient(165deg, var(--card-blue-top) 0%, #0f3b6a 45%, var(--card-blue-bottom) 100%);
  }
  .bokeh {
    position: absolute;
  }
  .card--front .bokeh {
    left: 60px;
    top: 0;
    width: 430px;
    height: 430px;
    background:
      radial-gradient(circle at 48% 22%, var(--bokeh-teal) 0, rgba(110,225,230,0.35) 22%, transparent 45%),
      radial-gradient(circle at 40% 60%, var(--bokeh-blue) 0, rgba(40,120,220,0.2) 30%, transparent 55%);
  }
  .card--back .bokeh {
    left: 40px;
    top: 0;
    width: 560px;
    height: 440px;
    background:
      radial-gradient(circle at 35% 22%, rgba(140, 240, 250, 0.85) 0, rgba(90, 200, 240, 0.4) 22%, transparent 42%),
      radial-gradient(circle at 40% 58%, rgba(70, 170, 240, 0.55) 0, rgba(40,120,220,0.2) 28%, transparent 50%),
      radial-gradient(circle at 80% 70%, rgba(90, 190, 240, 0.45) 0, transparent 16%);
  }
  .edge-band {
    position: absolute;
    right: 0;
    top: 0;
    width: 18px;
    height: 100%;
    background: linear-gradient(180deg, #1d4f7e 0%, var(--edge-blue) 50%, #6b8fb8 100%);
  }
  .identity {
    position: absolute;
    display: flex;
    align-items: center;
    gap: 12px;
  }
  .identity__mark {
    width: 18px;
    height: 18px;
    background: var(--accent-blue);
    flex: none;
  }
  .identity__name {
    color: var(--text-white);
    font-weight: 700;
    text-transform: uppercase;
    line-height: 1.1;
  }
  .card--front .identity { left: 560px; top: 80px; }
  .card--front .identity__name { font-size: 22px; width: 230px; }
  .card--back .identity { left: 560px; top: 250px; }
  .card--back .identity__name { font-size: 26px; width: 260px; }
  .person {
    position: absolute;
    left: 120px;
    top: 205px;
  }
  .person__name {
    color: var(--text-white);
    font-size: 54px;
    font-weight: 600;
    letter-spacing: -0.5px;
    text-transform: uppercase;
    line-height: 1;
  }
  .person__role {
    margin-top: 8px;
    color: var(--text-grey);
    font-size: 14px;
    letter-spacing: 9px;
    text-transform: uppercase;
  }
  .contacts {
    position: absolute;
    left: 560px;
    top: 250px;
    list-style: none;
    color: var(--text-white);
    font-size: 18px;
  }
  .contacts li { margin-bottom: 20px; }
  .contacts__label {
    color: var(--accent-blue);
    margin-right: 6px;
  }
  .website {
    position: absolute;
    left: 80px;
    bottom: 60px;
    color: var(--text-white);
    font-size: 22px;
    letter-spacing: 9px;
  }
</style>
</head>
<body>
<main class="sheet">
  <section class="card card--front" aria-label="Card front">
    <div class="bokeh" role="img" aria-label="Soft teal and blue out-of-focus light circles"></div>
    <div class="identity">
      <span class="identity__mark"></span>
      <span class="identity__name">Marni Voss Hospitality College</span>
    </div>
    <div class="person">
      <p class="person__name">Dena Whitby</p>
      <p class="person__role">Director</p>
    </div>
    <ul class="contacts">
      <li><span class="contacts__label">P</span>: 1300 561 437</li>
      <li><span class="contacts__label">M</span>: 0439 817 265</li>
      <li><span class="contacts__label">E</span>: info@marnivoss.com</li>
    </ul>
    <div class="edge-band"></div>
  </section>

  <section class="card card--back" aria-label="Card back">
    <div class="bokeh" role="img" aria-label="Bright cyan and blue out-of-focus light circles"></div>
    <div class="identity">
      <span class="identity__mark"></span>
      <span class="identity__name">Marni Voss Hospitality College</span>
    </div>
    <p class="website">www.marnivoss.com</p>
  </section>
</main>
</body>
</html>
```